We need a business card design for our residential home building company based out of East Tennessee and the Smoky Mountains. We have 30 years of experience, and we plan to build homes not only in the state of Tennessee, but out of state as well. We are a different kind of production home builder; we aim to build homes cost-effectively and efficiently but with the character, dignity, and charm of historic homes. Our homes have a timeless style with modern floorplans and features. We would like to see designs that embody a classic style with accents of gold, red, and blue. The resulting business card should convey elegance, strength, character, and trust as well as the careful balance of the old and new.
Motto: "Shaping Lasting Roots"
Reason: I would like to extend the deadline so that more changes can be made to the best designs.
Target Market(s)
Adults 40+ from the Northern states looking to settle in Tennessee.
Industry/Entity Type
Residential
Contact Information for Business Card
Birchwood Dwellworks, LLC
Marla Pettigrew | Director of Operations
20815 Thornbury Lane | Suite 300
Knoxville, TN 37091
Office: (865)413-2958
Mobile: (865)690-8142
Email: marla@birchwooddwellworks.example

```html
<!DOCTYPE html>
<html lang="en">
<head>
<meta charset="utf-8">
<title>Birchwood Dwellworks, LLC — Business Card</title>
<link rel="stylesheet" href="https://fonts.googleapis.com/css2?family=Source+Sans+3:wght@400;600;700&display=swap">
<style>
  :root {
    --backdrop: #e9e6e1;
    --card: #fdf1d0;
    --gold: #7d6a3d;
    --gold-soft: #c9b78a;
    --red: #e0201e;
    --blue: #3c7cc8;
    --peach: #f5b48a;
    --mist: #b9c3cf;
  }
  * { box-sizing: border-box; margin: 0; padding: 0; }
  html, body { width: 1200px; height: 1000px; overflow: hidden; }
  body {
    background: var(--backdrop);
    font-family: "Source Sans 3", Arial, sans-serif;
    color: var(--gold);
    position: relative;
  }
  .card {
    position: absolute;
    left: 265px;
    width: 665px;
    height: 397px;
    background: var(--card);
    box-shadow: 0 2px 8px rgba(0,0,0,0.18);
    overflow: hidden;
  }
  .card--front { top: 73px; }
  .card--back { top: 532px; }

  .brand {
    position: absolute;
    text-align: center;
    font-weight: 700;
    color: var(--gold);
    line-height: 1;
  }
  .brand__dot {
    display: block;
    margin: 0 auto 18px;
    border-radius: 50%;
    background: var(--gold);
  }
  .brand__main { display: block; letter-spacing: 2px; }
  .brand__sub { display: block; letter-spacing: 1px; margin-top: 6px; }

  .card--front .brand { left: 0; right: 0; top: 120px; }
  .card--front .brand__dot { width: 56px; height: 56px; }
  .card--front .brand__main { font-size: 54px; }
  .card--front .brand__sub { font-size: 24px; }

  .tagline {
    position: absolute;
    left: 0; right: 0; top: 348px;
    text-align: center;
    font-size: 17px;
    font-weight: 600;
    letter-spacing: 1.5px;
  }

  .floral-accent { position: absolute; }
  .floral-accent--peach { left: -40px; top: -30px; width: 150px; height: 200px; }
  .floral-accent--mist { right: -30px; bottom: -40px; width: 170px; height: 230px; }

  .card--back .brand { left: 60px; width: 220px; top: 115px; }
  .card--back .brand__dot { width: 44px; height: 44px; margin-bottom: 16px; }
  .card--back .brand__main { font-size: 38px; }
  .card--back .brand__sub { font-size: 17px; }

  .contact { position: absolute; left: 333px; top: 92px; }
  .contact__name { font-size: 21px; font-weight: 700; letter-spacing: 0.5px; line-height: 1; }
  .contact__title { font-size: 16px; font-weight: 600; margin-top: 4px; }
  .contact__address { font-size: 16px; font-weight: 700; margin-top: 24px; line-height: 22px; }
  .contact__list { list-style: none; margin-top: 14px; font-size: 16px; font-weight: 600; }
  .contact__list li { display: flex; align-items: center; height: 30px; }
  .contact__list svg { width: 16px; height: 16px; margin-right: 7px; flex: none; }
</style>
</head>
<body>
  <section class="card card--front">
    <div class="brand">
      <span class="brand__dot"></span>
      <span class="brand__main">BIRCHWOOD</span>
      <span class="brand__sub">Dwellworks, LLC</span>
    </div>
    <p class="tagline">Shaping Lasting Roots</p>
  </section>

  <section class="card card--back">
    <svg class="floral-accent floral-accent--peach" role="img" aria-label="Faded floral accent" viewBox="0 0 150 200">
      <defs><radialGradient id="peachGlow"><stop offset="0" stop-color="#f5b48a" stop-opacity="0.9"/><stop offset="1" stop-color="#f5b48a" stop-opacity="0"/></radialGradient></defs>
      <ellipse cx="75" cy="100" rx="75" ry="100" fill="url(#peachGlow)"/>
    </svg>
    <svg class="floral-accent floral-accent--mist" role="img" aria-label="Faded floral accent" viewBox="0 0 170 230">
      <defs><radialGradient id="mistGlow"><stop offset="0" stop-color="#b9c3cf" stop-opacity="0.95"/><stop offset="1" stop-color="#b9c3cf" stop-opacity="0"/></radialGradient></defs>
      <ellipse cx="85" cy="115" rx="85" ry="115" fill="url(#mistGlow)"/>
    </svg>

    <div class="brand">
      <span class="brand__dot"></span>
      <span class="brand__main">BIRCHWOOD</span>
      <span class="brand__sub">Dwellworks, LLC</span>
    </div>

    <div class="contact">
      <p class="contact__name">MARLA PETTIGREW</p>
      <p class="contact__title">Director of Operations</p>
      <p class="contact__address">20815 Thornbury Lane | Suite 300<br>Knoxville, TN 37091</p>
      <ul class="contact__list">
        <li>
          <svg viewBox="0 0 16 16" aria-hidden="true"><rect x="4" y="1" width="8" height="14" rx="1.5" fill="none" stroke="var(--red)" stroke-width="1.6"/><circle cx="8" cy="12.5" r="0.9" fill="var(--red)"/></svg>
          (865)690-8142
        </li>
        <li>
          <svg viewBox="0 0 16 16" aria-hidden="true"><path d="M1 6c0-2 3-3.5 7-3.5S15 4 15 6v1.5h-3.5V6H4.5v1.5H1z" fill="var(--red)"/><path d="M3.5 8.5h9l1 5.5h-11z" fill="var(--red)"/><circle cx="8" cy="11" r="1.4" fill="var(--card)"/></svg>
          (865)413-2958
        </li>
        <li>
          <svg viewBox="0 0 16 16" aria-hidden="true"><rect x="1" y="3.5" width="14" height="9.5" fill="var(--blue)"/><path d="M1 3.5l7 5.5 7-5.5" fill="none" stroke="var(--card)" stroke-width="1.2"/></svg>
          marla@birchwooddwellworks.example
        </li>
      </ul>
    </div>
  </section>
</body>
</html>
```